Business card for new consulting business - Brenvale Holdings Pty Ltd.

Consulting in the areas of Occupational Health, Safety and Community Relations in the resources (mining) industries. The consultant (me) will work both within Australia and overseas jurisdictions such as South East Asia, Africa , South America etc, often working with third world indigenous communities. The design should suggest a high level of social and environmental responsibility.

```html
<!DOCTYPE html>
<html lang="en">
<head>
<meta charset="utf-8">
<title>Brenvale Holdings Pty Ltd — Business Card</title>
<link rel="stylesheet" href="https://fonts.googleapis.com/css2?family=Saira+Semi+Condensed:wght@600;700&display=swap">
<style>
  :root {
    --backdrop: #ecebe8;
    --card: #ffffff;
    --ember: #ef4614;
    --charcoal: #2a2221;
    --card-shadow: rgba(0, 0, 0, 0.12);
  }
  * { box-sizing: border-box; margin: 0; padding: 0; }
  html, body {
    width: 1200px;
    height: 840px;
    overflow: hidden;
    background: var(--backdrop);
  }
  .business-card {
    position: absolute;
    left: 160px;
    top: 150px;
    width: 880px;
    height: 540px;
    background: var(--card);
    box-shadow: 0 6px 24px var(--card-shadow);
    overflow: hidden;
  }
  .brand {
    position: absolute;
    left: 70px;
    top: 120px;
    width: 330px;
    display: flex;
    flex-direction: column;
    align-items: center;
  }
  .brand-dot {
    width: 150px;
    height: 150px;
    border-radius: 50%;
    background: var(--ember);
  }
  .brand-name {
    margin-top: 34px;
    font-family: "Saira Semi Condensed", "Arial Narrow", sans-serif;
    font-weight: 700;
    color: var(--charcoal);
    text-align: center;
    line-height: 1;
    text-transform: uppercase;
  }
  .brand-name .primary {
    display: block;
    font-size: 56px;
    letter-spacing: 1px;
  }
  .brand-name .secondary {
    display: block;
    margin-top: 8px;
    font-size: 20px;
    letter-spacing: 5px;
  }
  .contact-list {
    position: absolute;
    left: 470px;
    top: 150px;
    width: 390px;
    list-style: none;
    font-family: "Saira Semi Condensed", "Arial Narrow", sans-serif;
    font-weight: 600;
    font-size: 20px;
    letter-spacing: 1.5px;
    color: var(--charcoal);
    text-transform: uppercase;
    line-height: 1.15;
  }
  .contact-item {
    display: flex;
    align-items: center;
    gap: 22px;
    margin-bottom: 24px;
  }
  .contact-marker {
    flex: none;
    width: 30px;
    height: 11px;
    border-radius: 50%;
  }
  .marker-ember { background: var(--ember); }
  .marker-charcoal { background: var(--charcoal); }
  .band-ember {
    position: absolute;
    left: 0;
    bottom: 0;
    width: 500px;
    height: 16px;
    background: var(--ember);
  }
  .band-charcoal {
    position: absolute;
    left: 500px;
    bottom: 16px;
    right: 0;
    height: 22px;
    background: var(--charcoal);
  }
</style>
</head>
<body>
  <article class="business-card">
    <div class="brand">
      <div class="brand-dot"></div>
      <h1 class="brand-name">
        <span class="primary">Brenvale</span>
        <span class="secondary">Holdings Pty Ltd</span>
      </h1>
    </div>

    <ul class="contact-list">
      <li class="contact-item">
        <span class="contact-marker marker-ember"></span>
        <span>amarsh@brenvale.com.au</span>
      </li>
      <li class="contact-item">
        <span class="contact-marker marker-charcoal"></span>
        <span>brenvale.com.au</span>
      </li>
      <li class="contact-item">
        <span class="contact-marker marker-ember"></span>
        <span>Harlow Street,<br>Kelmont, VIC 3142</span>
      </li>
    </ul>

    <div class="band-ember"></div>
    <div class="band-charcoal"></div>
  </article>
</body>
</html>
```